Webdesign für freiberuflichen Statiker
Zielgruppe
Ich bin seit 2021 freiberuflicher Statiker. Ich arbeite mit anderen Freelancern / Partnern / Firmen zusammen und lasse von ihnen z.B. Pläne zeichnen. Meine aktuelle Website habe ich selbst designed, mit Wordpress. Diese soll nun aber komplett neu gestaltet werden. Meine Domain www.vendrik-statik.de möchte ich möglichst behalten.
Meine Zielgruppe sind Architekturbüros, Bauträger, private und öffentliche Bauherren. Sie sollen vor allem einen visuellen Eindruck von unserer Arbeit bekommen - durch Fotos (und einem Video auf der Startseite) von Baustellen, von unseren 3D-Modellen oder Berechnungsmodellen.
Aufgabenstellung
Es gibt bereits ein neues Logo. Dieses werde ich mit anhängen. Außerdem habe ich eine pdf-Datei vorbereitet ('SBV_Inhalte Website'), die den groben Aufbau der Website vorgibt und der die Texte entnommen werden können. Auf der ersten Seite des Dokuments stehen außerdem 3 Beispiel-Websites, die ich gut finde und an denen Ihr euch orientieren könnt. Die Farbwahl kann sehr schlicht gehalten werden - ähnlich wie bei den 3 Beispiel-Seiten. Ich liefere eigene Bilder mit, für projektunabhängige Inhalte können aber auch andere Bilder verwendet werden.

```html
<!DOCTYPE html>
<html lang="de">
<head>
<meta charset="utf-8">
<title>SBV – Projekte</title>
<link href="https://fonts.googleapis.com/css2?family=Montserrat:wght@400;500;600;700&display=swap" rel="stylesheet">
<style>
  :root {
    --ink: #000000;
    --muted: #8a8a8a;
    --rule: #a6a6a6;
    --paper: #ffffff;
    --footer: #000000;
    --footer-text: #ffffff;
  }
  * { margin: 0; padding: 0; box-sizing: border-box; }
  html, body { width: 1200px; height: 1133px; overflow: hidden; background: var(--paper); }
  body { position: relative; font-family: "Montserrat", sans-serif; color: var(--ink); }

  .site-header { position: absolute; left: 0; top: 0; width: 1200px; height: 95px; border-bottom: 2px solid var(--rule); }
  .brand { position: absolute; left: 53px; top: 20px; font-weight: 700; font-size: 40px; letter-spacing: 1px; color: var(--ink); }
  .nav-divider { position: absolute; left: 712px; top: 0; width: 2px; height: 95px; background: var(--rule); }
  .main-nav a { position: absolute; top: 36px; font-size: 19px; font-weight: 600; text-decoration: none; color: var(--muted); transform: translateX(-50%); }
  .main-nav a.active { color: var(--ink); font-weight: 700; }

  .page-intro .subheadline { position: absolute; left: 44px; top: 145px; font-size: 18px; font-weight: 500; color: var(--muted); letter-spacing: 0.5px; }
  .page-intro h1 { position: absolute; left: 44px; top: 173px; font-size: 68px; font-weight: 500; letter-spacing: 2px; line-height: 1; }

  .project-row { position: absolute; left: 0; width: 1200px; border-bottom: 2px solid var(--rule); }
  .row-1 { top: 261px; height: 309px; }
  .row-2 { top: 658px; height: 338px; }
  .project { position: absolute; top: 0; width: 400px; }
  .project-image { width: 400px; height: 224px; }
  .project + .project .project-image { border-left: 1px solid #ffffff; }
  .project-meta { padding: 16px 0 0 43px; }
  .location { display: flex; align-items: center; gap: 8px; font-size: 19px; font-weight: 500; color: var(--muted); letter-spacing: 0.5px; }
  .location svg { width: 19px; height: 19px; }
  .title { margin-top: 6px; font-size: 19px; font-weight: 600; line-height: 28px; letter-spacing: 0.4px; }

  .img-hotel { background: linear-gradient(180deg, #6e6a66 0%, #a8a39c 18%, #d9d7d3 40%, #c9c6c1 65%, #9c958a 85%, #7d7567 100%); }
  .img-school { background: linear-gradient(180deg, #e6ebee 0%, #d7dde0 22%, #c98f6e 34%, #ddcfb8 50%, #c9a684 70%, #b98f72 85%, #d2ccbf 100%); }
  .img-corner { background: linear-gradient(180deg, #dbe6ef 0%, #b9c9d4 15%, #3f5e66 35%, #2f4a52 60%, #56636a 80%, #262b30 100%); }
  .img-hall { background: linear-gradient(180deg, #cfdce6 0%, #e7edf0 30%, #9aa98a 55%, #cbb9a0 70%, #a9a397 88%, #8b8a82 100%); }
  .img-plant { background: linear-gradient(180deg, #aeb7bf 0%, #8e98a0 25%, #4fb35e 45%, #5d8a8f 62%, #c8ccd0 78%, #9ea3a7 100%); }
  .img-kita { background: linear-gradient(180deg, #dce6ec 0%, #cfd9de 20%, #6f8a52 38%, #c98a4a 48%, #8f9a74 62%, #a9a99c 82%, #96978c 100%); }

  .site-footer { position: absolute; left: 0; top: 1085px; width: 1200px; height: 48px; background: var(--footer); color: var(--footer-text); font-size: 13px; }
  .copyright { position: absolute; left: 45px; top: 16px; }
  .footer-nav a { position: absolute; top: 15px; color: var(--footer-text); text-decoration: none; font-size: 14px; letter-spacing: 0.3px; }
</style>
</head>
<body>

<header class="site-header">
  <div class="brand">SBV</div>
  <div class="nav-divider"></div>
  <nav class="main-nav">
    <a href="#" style="left:784px">OFFICE</a>
    <a href="#" class="active" style="left:934px">PROJEKTE</a>
    <a href="#" style="left:1101px">EXPERTISE</a>
  </nav>
</header>

<section class="page-intro">
  <div class="subheadline">SUBHEADLINE</div>
  <h1>PROJEKTE</h1>
</section>

<svg width="0" height="0" style="position:absolute">
  <defs>
    <symbol id="map-pin" viewBox="0 0 20 20">
      <path d="M2 7 L6 5.5 L10 7 L14 5.5 L18 7 V18 L14 16.5 L10 18 L6 16.5 L2 18 Z" fill="none" stroke="#8a8a8a" stroke-width="1.2"/>
      <path d="M12 2 a3 3 0 0 1 3 3 c0 2.3 -3 5.5 -3 5.5 s-3 -3.2 -3 -5.5 a3 3 0 0 1 3 -3 z" fill="#fff" stroke="#8a8a8a" stroke-width="1.2"/>
      <circle cx="12" cy="5" r="1" fill="#8a8a8a"/>
    </symbol>
  </defs>
</svg>

<section class="project-row row-1">
  <article class="project" style="left:0">
    <div class="project-image img-hotel" role="img" aria-label="Luftbild einer Hotel-Baustelle mit eingerüstetem Rohbau an einer Kreuzung"></div>
    <div class="project-meta">
      <div class="location"><svg><use href="#map-pin"/></svg>VELBERT</div>
      <div class="title">NEUBAU HOTEL MERKUR</div>
    </div>
  </article>
  <article class="project" style="left:400px">
    <div class="project-image img-school" role="img" aria-label="Visualisierung einer Grundschule mit Backsteinfassade und Bäumen"></div>
    <div class="project-meta">
      <div class="location"><svg><use href="#map-pin"/></svg>BELITZ-HEILSTÄTTEN</div>
      <div class="title">NEUBAU GRUNDSCHULE</div>
    </div>
  </article>
  <article class="project" style="left:800px">
    <div class="project-image img-corner" role="img" aria-label="Visualisierung eines runden Geschäftshauses mit Glasfassade an einer Straßenecke"></div>
    <div class="project-meta">
      <div class="location"><svg><use href="#map-pin"/></svg>BERLIN</div>
      <div class="title">UMBAU SPREE ECK</div>
    </div>
  </article>
</section>

<section class="project-row row-2">
  <article class="project" style="left:0">
    <div class="project-image img-hall" role="img" aria-label="Visualisierung einer Sporthalle hinter einem Platz mit Bäumen"></div>
    <div class="project-meta">
      <div class="location"><svg><use href="#map-pin"/></svg>BELITZ-HEILSTÄTTEN</div>
      <div class="title">NEUBAU SPORTHALLE</div>
    </div>
  </article>
  <article class="project" style="left:400px">
    <div class="project-image img-plant" role="img" aria-label="Industrieanlage mit grünen Rohrleitungen und Technikern"></div>
    <div class="project-meta">
      <div class="location"><svg><use href="#map-pin"/></svg>ZÖRBIG</div>
      <div class="title">ERWEITERUNG MESSWARTE<br>VENTARA AG</div>
    </div>
  </article>
  <article class="project" style="left:800px">
    <div class="project-image img-kita" role="img" aria-label="Visualisierung einer Kita mit Garten und Parkplatz aus der Vogelperspektive"></div>
    <div class="project-meta">
      <div class="location"><svg><use href="#map-pin"/></svg>KETZIN</div>
      <div class="title">NEUBAU KITA</div>
    </div>
  </article>
</section>

<footer class="site-footer">
  <div class="copyright">© 2024 farbwerk-media.com</div>
  <nav class="footer-nav">
    <a href="#" style="left:834px">KONTAKT</a>
    <a href="#" style="left:950px">IMPRESSUM</a>
    <a href="#" style="left:1067px">DATENSCHUTZ</a>
  </nav>
</footer>

</body>
</html>
```